Business Card Design

I require the design of business cards using my exisiting logo.

It is essential that the designer has experience with various print processes (foil stamping etc) and different paper stock.

The design is to blend in with current packaging and display unit. (Images will be provided).
A swing tag and certificate of authenticity design will als be required at a later stage.

Details which need to be included on the card are:
- Contact Name
- Position in Company
- Address
- Contact Number
- Email Address
- Web Address

Ideally I would prefer the background (both sides) to be greyish colour (offset printing or if you can suggest greyish paperstock) with silver foiling on the front and either black or metallic silver on the back.

Or another option would be grey background on the front and either white or black on the the back.

* The business card can be portrait or landscape.

Printers specifications:
Bleed 3mm
Trim Marks
Seperate file for foil printing

This task is for someone who is creative and enjoys working with fashion and luxury items!
_______________________________________________

I will require business cards designs for 2 different business and would hope to work with the same designer.

Please note I had asked for a grey colour at least on one of the sides. However I keep on getting black and white designs.   

Industry/Entity Type

Business

Requirements
Must have
• - Double sided business card
- Luxury feel
- Foil Print Priniting

- Would prefer at least grey background at least on one side of the card.

- The business card can be portrait or landscape.
Nice to have
• *The business card can be portrait or landscape.
Should not have
• - Bright Colours
- Alterations to logo

```html
<!DOCTYPE html>
<html lang="en">
<head>
<meta charset="utf-8">
<title>Ora Gems – Business Card</title>
<link href="https://fonts.googleapis.com/css2?family=Roboto+Condensed:wght@300&display=swap" rel="stylesheet">
<style>
  :root {
    --stage: #f2f1ef;
    --card-grey: #c6c7c8;
    --card-dark: #0e0e0e;
    --ink: #222222;
    --ink-soft: #3f3f3f;
    --foil: #c8c9cb;
    --rule: #2e2e2e;
  }
  * { margin: 0; padding: 0; box-sizing: border-box; }
  html, body {
    width: 1200px;
    height: 880px;
    overflow: hidden;
    background: var(--stage);
    font-family: "Roboto Condensed", "Arial Narrow", sans-serif;
    font-weight: 300;
  }
  .stage {
    position: relative;
    width: 1200px;
    height: 880px;
  }
  .card {
    position: absolute;
    width: 540px;
    height: 309px;
    box-shadow: 0 6px 18px rgba(0,0,0,0.18);
  }
  /* Back side: black with silver foil */
  .card-back {
    left: 40px;
    top: 320px;
    background: var(--card-dark);
    display: flex;
    align-items: center;
    justify-content: center;
  }
  .back-brand {
    display: flex;
    align-items: center;
    gap: 18px;
    color: var(--foil);
  }
  .back-brand .mark {
    width: 44px;
    height: 44px;
    border: 1.5px solid var(--foil);
    border-radius: 50%;
  }
  .back-brand .name {
    font-size: 46px;
    letter-spacing: 1px;
  }
  /* Front side: grey stock */
  .card-front {
    left: 620px;
    top: 250px;
    background: var(--card-grey);
    color: var(--ink);
  }
  .front-brand {
    position: absolute;
    left: 34px;
    top: 70px;
    display: flex;
    flex-direction: column;
    align-items: flex-start;
    gap: 14px;
  }
  .front-brand .mark {
    width: 38px;
    height: 38px;
    border: 1.2px solid var(--ink);
    border-radius: 50%;
    margin-left: 50px;
  }
  .front-brand .name {
    font-size: 36px;
    letter-spacing: 0.5px;
    color: var(--ink-soft);
  }
  .holder {
    position: absolute;
    left: 282px;
    top: 84px;
    width: 222px;
    border-bottom: 1px solid var(--rule);
    padding-bottom: 10px;
  }
  .holder .person {
    font-size: 27px;
    line-height: 1;
    letter-spacing: 0.3px;
  }
  .holder .role {
    font-size: 11px;
    color: var(--ink-soft);
    margin-top: 4px;
  }
  .contacts {
    position: absolute;
    left: 238px;
    top: 188px;
    display: grid;
    grid-template-columns: 70px auto;
    row-gap: 5px;
    font-size: 12.5px;
    color: var(--ink);
  }
  .contacts dt { color: var(--ink-soft); }
</style>
</head>
<body>
<main class="stage">
  <section class="card card-back" aria-label="Business card, back">
    <div class="back-brand">
      <span class="mark" aria-hidden="true"></span>
      <span class="name">ORA GEMS</span>
    </div>
  </section>

  <section class="card card-front" aria-label="Business card, front">
    <div class="front-brand">
      <span class="mark" aria-hidden="true"></span>
      <span class="name">ORA GEMS</span>
    </div>
    <div class="holder">
      <p class="person">MARTIN VALE</p>
      <p class="role">manager</p>
    </div>
    <dl class="contacts">
      <dt>Phone:</dt><dd>0971-48-2256</dd>
      <dt>E-mail:</dt><dd>office@ora-gems.com</dd>
      <dt>Website:</dt><dd>www.ora-gems.com</dd>
      <dt>Address:</dt><dd>Your Address Goes Here, City, Country</dd>
    </dl>
  </section>
</main>
</body>
</html>
```